Prospective Client Marketing Power Point Refresh/Update

My company has been using the attached power point to share with prospective clients. I'd like to have it refreshed with new graphics and style. The color pallet is something we'd like to stay true to. We are looking for your design expertise and ideas to help us update the look of the PP. We work with high wealth clients and want to have this reflect the value we can bring to the table.

Target Market(s)

Wealth Management Clients

Industry/Entity Type

Financial Advisors

Font styles to use
Sans Serif

Colors
0054AA
0677BA
7BADD7
CADEEF
E8F1F8
0094D4
00A9DD
6FCCEA
C7EBF8
E9F6FB

Requirements
Must have
• Updated look
Nice to have
• Fresh graphics

```html
<!DOCTYPE html>
<html lang="en">
<head>
<meta charset="utf-8">
<title>Clearpath Wealth – Client Presentation</title>
<link href="https://fonts.googleapis.com/css2?family=Montserrat:wght@400;500;600;700;800&family=Open+Sans:wght@400;600&display=swap" rel="stylesheet">
<style>
:root{
  --navy:#0054AA;
  --blue:#0677BA;
  --sky:#0094D4;
  --cyan:#00A9DD;
  --mist:#7BADD7;
  --pale:#CADEEF;
  --ice:#E8F1F8;
  --frost:#E9F6FB;
  --ink:#1d1d1d;
  --text:#333;
  --green:#4E7F2B;
  --stage:#7b7b7b;
}
*{margin:0;padding:0;box-sizing:border-box}
html,body{width:1200px;height:4231px;overflow:hidden;background:var(--stage)}
body{position:relative;font-family:'Open Sans',sans-serif;color:var(--text)}
.slide{position:absolute;left:60px;width:1080px;height:607px;overflow:hidden;background:#fff}
.slide svg.deco{position:absolute;inset:0}
.wordmark{font-family:'Montserrat',sans-serif;font-weight:700;color:var(--navy);display:flex;align-items:center;gap:12px;white-space:nowrap}
.wordmark .dot{width:22px;height:22px;border-radius:50%;background:var(--navy);flex:none}
.photo{position:absolute}
.heading{position:absolute;left:113px;top:34px;font-family:'Montserrat',sans-serif;font-weight:700;font-size:27px;line-height:36px;color:var(--ink);letter-spacing:.3px}
.heading span{color:var(--sky)}
.caption{position:absolute;font-size:11.5px;line-height:22px;text-align:center;color:#444}

/* slide 1 */
.s-welcome{top:84px;background:#222}
.s-welcome .intro{position:absolute;left:0;right:0;text-align:center;color:#fff;font-family:'Montserrat',sans-serif}
.s-welcome .pre{top:375px;font-size:34px;font-weight:400;letter-spacing:1px}
.s-welcome .title{top:425px;font-size:54px;font-weight:700}
.s-welcome .sub{top:505px;font-size:20px;font-family:'Open Sans',sans-serif}
.socials{position:absolute;right:22px;bottom:20px;display:flex;gap:13px}
.socials i{width:38px;height:38px;border:2px solid #fff;border-radius:50%;display:block}

/* slide 2 */
.s-relation{top:760px;background:linear-gradient(100deg,#fff 0%,var(--ice) 55%,#d5e4f1 100%)}
.feature-icon{position:absolute;width:88px;height:88px;border-radius:50%;background:var(--navy);display:flex;align-items:center;justify-content:center}

/* slide 3 */
.s-services{top:1448px;background:linear-gradient(180deg,#fff,var(--frost))}
.intro-copy{position:absolute;left:113px;top:76px;font-size:11.5px;line-height:22px;color:#444}
.service{position:absolute;font-family:'Montserrat',sans-serif;font-size:17px;line-height:25px;color:#222}

/* slide 4 */
.s-tech{top:2138px}
.tool{position:absolute;top:241px;width:256px;height:268px;color:#fff;text-align:center;font-size:11.5px;line-height:22.5px;padding:98px 12px 0}
.tool .seal{position:absolute;left:50%;top:-66px;transform:translateX(-50%);width:132px;height:132px;border-radius:50%;background:#fff;box-shadow:0 4px 12px rgba(0,0,0,.18);display:flex;align-items:center;justify-content:center;font-family:'Montserrat',sans-serif;font-weight:700;font-size:19px;color:var(--navy)}

/* slide 5 */
.s-process{top:2840px;background:linear-gradient(180deg,#fff,var(--ice))}
.step-ring{position:absolute;top:241px;width:112px;height:112px;border-radius:50%;border:2px solid #8a8a8a;background:#fff;display:flex;align-items:center;justify-content:center}
.step-label{position:absolute;top:388px;width:150px;text-align:center;font-family:'Montserrat',sans-serif;font-weight:600;font-size:12px;line-height:20px;color:#333}
.tagline{position:absolute;left:0;right:0;top:462px;text-align:center;font-family:'Montserrat',sans-serif;font-weight:500;font-size:20px;color:#222}
.cta{position:absolute;top:518px;height:70px;border-radius:4px;color:#fff;display:flex;align-items:center;justify-content:center;text-align:center;font-family:'Montserrat',sans-serif;font-weight:700;font-size:14px;line-height:22px}

/* slide 6 */
.s-thanks{top:3538px}
.thanks{position:absolute;left:49px;top:336px;font-family:'Montserrat',sans-serif;font-weight:700;font-size:40px;color:var(--blue)}
.presenter{position:absolute;left:49px;top:400px;font-family:'Montserrat',sans-serif;font-weight:600;font-size:20px;color:#333}
.contacts{position:absolute;left:49px;top:444px;width:260px;list-style:none}
.contacts li{display:flex;align-items:flex-start;gap:14px;font-size:11.5px;line-height:17px;color:#444;height:37px;white-space:nowrap}
.contacts svg{flex:none;margin-top:1px}
</style>
</head>
<body>

<!-- Welcome -->
<section class="slide s-welcome">
  <div class="photo" role="img" aria-label="Dark photo of two advisors in conversation" style="inset:0;background:linear-gradient(120deg,#3a3a3a,#1b1b1b 60%,#2b2b2b)"></div>
  <svg class="deco" width="1080" height="607" viewBox="0 0 1080 607">
    <polygon points="0,0 1080,0 1080,60 492,237 0,0" fill="#fff"/>
    <polygon points="0,0 492,237 0,420" fill="#1a9be0"/>
    <polygon points="492,237 1080,60 1080,90 520,250" fill="#0b4fb0"/>
    <polygon points="900,0 1080,0 1080,60 1000,80" fill="#0b4fb0"/>
    <circle cx="496" cy="266" r="44" fill="#fff"/>
    <circle cx="496" cy="266" r="36" fill="var(--navy)"/>
  </svg>
  <div class="wordmark" style="position:absolute;left:390px;top:100px;font-size:38px"><span class="dot"></span>Clearpath Wealth</div>
  <div class="intro pre">WELCOME TO</div>
  <div class="intro title">CLEARPATH WEALTH</div>
  <div class="intro sub">Your personal financial website</div>
  <div class="socials"><i></i><i></i><i></i><i></i></div>
</section>

<!-- Relationship -->
<section class="slide s-relation">
  <div class="photo" role="img" aria-label="Faded photo of a hand over financial charts" style="right:0;top:0;width:520px;height:607px;background:linear-gradient(90deg,rgba(200,218,235,0),rgba(170,195,220,.55))"></div>
  <svg class="deco" width="1080" height="607" viewBox="0 0 1080 607">
    <polygon points="0,0 110,0 0,160" fill="var(--sky)"/>
    <polygon points="60,0 110,0 80,35" fill="#111"/>
    <circle cx="60" cy="48" r="28" fill="#fff"/>
    <polygon points="760,607 1080,520 1080,607" fill="var(--navy)"/>
    <polygon points="900,607 1080,575 1080,607" fill="#111"/>
  </svg>
  <h2 class="heading">CLEARPATH WEALTH<br><span>RELATIONSHIP</span></h2>

  <div class="feature-icon" style="left:206px;top:143px"><svg width="44" height="44" viewBox="0 0 44 44" fill="none" stroke="#fff" stroke-width="2"><circle cx="24" cy="14" r="8"/><path d="M4 34h10l8 4 14-8-4-3-10 4"/></svg></div>
  <div class="feature-icon" style="left:496px;top:143px"><svg width="44" height="44" viewBox="0 0 44 44" fill="none" stroke="#fff" stroke-width="2"><rect x="10" y="6" width="24" height="32" rx="2"/><path d="M15 30v-6M21 30v-10M27 30v-14"/></svg></div>
  <div class="feature-icon" style="left:788px;top:143px"><svg width="44" height="44" viewBox="0 0 44 44" fill="none" stroke="#fff" stroke-width="2"><path d="M22 5l13 5v9c0 9-6 15-13 19C15 34 9 28 9 19v-9z"/><path d="M16 21l5 5 8-9"/></svg></div>
  <div class="caption" style="left:150px;top:250px;width:200px">Providing the highest level of<br>wealth advisory services.</div>
  <div class="caption" style="left:398px;top:250px;width:284px">There are so many financial decisions that impact<br>multiple areas of an individual's balance<br>sheet exposing you to a potentially costly mistake.</div>
  <div class="caption" style="left:728px;top:250px;width:208px">As an independent Registered<br>Investment Advisor, we follow the<br>highest financial standards.</div>

  <div class="feature-icon" style="left:206px;top:348px"><svg width="44" height="44" viewBox="0 0 44 44" fill="none" stroke="#fff" stroke-width="2"><path d="M4 20l8-8 8 4 6-4 14 8M10 22l10 10 4-2 8-6"/></svg></div>
  <div class="feature-icon" style="left:496px;top:348px"><svg width="44" height="44" viewBox="0 0 44 44" fill="none" stroke="#fff" stroke-width="2.5"><circle cx="22" cy="22" r="15"/><circle cx="22" cy="22" r="9"/><circle cx="22" cy="22" r="3" fill="#fff"/></svg></div>
  <div class="feature-icon" style="left:788px;top:348px"><svg width="44" height="44" viewBox="0 0 44 44" fill="none" stroke="#fff" stroke-width="2"><path d="M10 36V26M18 36V20M26 36V24M34 36V14M8 22l10-8 8 6 12-12"/></svg></div>
  <div class="caption" style="left:150px;top:455px;width:200px">We love being a trusted<br>advisor to deliver exceptional<br>service.</div>
  <div class="caption" style="left:398px;top:455px;width:284px">Our goal is to give you the peace<br>of mind that all aspects of your<br>financial picture are being taken</div>
  <div class="caption" style="left:728px;top:455px;width:208px">We work on a fee-only basis and<br>do not sell commission-based or<br>proprietary products or receive<br>kickbacks of any kind.</div>
</section>

<!-- Services -->
<section class="slide s-services">
  <div class="photo" role="img" aria-label="Faded tablet showing financial charts" style="left:60px;top:140px;width:1000px;height:420px;background:radial-gradient(ellipse at 50% 55%,rgba(202,222,239,.6),rgba(255,255,255,0) 70%)"></div>
  <svg class="deco" width="1080" height="607" viewBox="0 0 1080 607">
    <polygon points="0,0 110,0 0,160" fill="var(--sky)"/>
    <polygon points="60,0 110,0 80,35" fill="#111"/>
    <circle cx="60" cy="48" r="28" fill="#fff"/>
    <polygon points="760,607 1080,520 1080,607" fill="var(--navy)"/>
    <polygon points="900,607 1080,575 1080,607" fill="#111"/>
    <g transform="rotate(-112 540 342)" fill="none" stroke-width="106">
      <circle cx="540" cy="342" r="132" stroke="#0b3f94" stroke-dasharray="99 731" stroke-dashoffset="0"/>
      <circle cx="540" cy="342" r="132" stroke="#0f57b3" stroke-dasharray="99 731" stroke-dashoffset="-103.7"/>
      <circle cx="540" cy="342" r="132" stroke="#3477c6" stroke-dasharray="99 731" stroke-dashoffset="-207.4"/>
      <circle cx="540" cy="342" r="132" stroke="#6a9ed6" stroke-dasharray="99 731" stroke-dashoffset="-311.1"/>
      <circle cx="540" cy="342" r="132" stroke="#0b66c0" stroke-dasharray="99 731" stroke-dashoffset="-414.8"/>
      <circle cx="540" cy="342" r="132" stroke="#1c8cda" stroke-dasharray="99 731" stroke-dashoffset="-518.5"/>
      <circle cx="540" cy="342" r="132" stroke="#3aa6e6" stroke-dasharray="99 731" stroke-dashoffset="-622.2"/>
      <circle cx="540" cy="342" r="132" stroke="#1c6fc2" stroke-dasharray="99 731" stroke-dashoffset="-725.9"/>
    </g>
    <circle cx="540" cy="342" r="80" fill="#fff"/>
    <circle cx="540" cy="342" r="72" fill="#eef2f6"/>
  </svg>
  <div class="wordmark" style="position:absolute;left:484px;top:330px;font-size:15px;gap:6px"><span class="dot" style="width:10px;height:10px"></span>Clearpath</div>
  <h2 class="heading">WHAT DO <span>WE DO?</span></h2>
  <p class="intro-copy">We have the expertise and experience to provide an<br>exceptional personal CFO relationship.</p>
  <div class="service" style="left:63px;top:223px">Tax Planning &amp; Compliance</div>
  <div class="service" style="left:63px;top:293px">Investment Management</div>
  <div class="service" style="left:63px;top:363px">Executive Compensation &amp;<br>Benefits</div>
  <div class="service" style="left:63px;top:446px">Retirement Planning</div>
  <div class="service" style="left:806px;top:223px">Education</div>
  <div class="service" style="left:806px;top:293px">Insurance</div>
  <div class="service" style="left:806px;top:363px">Philanthropy</div>
  <div class="service" style="left:806px;top:429px">Cash Management &amp;<br>Budgeting</div>
</section>

<!-- Technology -->
<section class="slide s-tech">
  <div class="photo" role="img" aria-label="Faded photo of a team meeting in a bright office" style="inset:0;background:linear-gradient(90deg,#f4f7fa,#e7edf3 50%,#dfe6ee)"></div>
  <svg class="deco" width="1080" height="607" viewBox="0 0 1080 607">
    <polygon points="0,0 110,0 0,160" fill="var(--sky)"/>
    <polygon points="60,0 110,0 80,35" fill="#111"/>
    <circle cx="60" cy="48" r="28" fill="#fff"/>
    <polygon points="760,607 1080,510 1080,607" fill="var(--navy)"/>
    <polygon points="900,607 1080,570 1080,607" fill="#111"/>
  </svg>
  <h2 class="heading">TOP TIER TECHNOLOGY TO BRING<br><span>BEST IN CLASS SERVICE</span></h2>
  <div class="tool" style="left:118px;background:#1b95d8"><div class="seal">Quantra</div>Quantra is the firm's principal research platform that can deliver institutional level equity and fixed income coverage of 42,000 equities, mutual funds and ETFs in addition to 400,000 economic tools and indicators.</div>
  <div class="tool" style="left:412px;background:#0b56ad"><div class="seal">Portvue</div>Portvue is an advanced, cloud-based financial management solution that allows clients to track and monitor all their investments and wealth in one place, including live reporting on balances, performance, asset allocation, asset location and detailed holding information.</div>
  <div class="tool" style="left:708px;background:#1b95d8"><div class="seal">TaxWell</div>Tax software used by the nation's top tax firms and businesses for an integrated tax and solution to deliver exceptional tax preparation service to achieve solutions designed to minimize a client's income, gift and estate taxes.</div>
</section>

<!-- Process -->
<section class="slide s-process">
  <svg class="deco" width="1080" height="607" viewBox="0 0 1080 607">
    <polygon points="0,0 110,0 0,160" fill="var(--sky)"/>
    <polygon points="60,0 110,0 80,35" fill="#111"/>
    <circle cx="60" cy="48" r="28" fill="#fff"/>
    <polygon points="760,607 1080,520 1080,607" fill="var(--navy)"/>
    <polygon points="900,607 1080,575 1080,607" fill="#111"/>
    <g>
      <polygon points="113,162 262,162 277,177 262,192 113,192 128,177" fill="var(--navy)"/>
      <polygon points="286,162 435,162 450,177 435,192 286,192 301,177" fill="var(--sky)"/>
      <polygon points="459,162 608,162 623,177 608,192 459,192 474,177" fill="var(--navy)"/>
      <polygon points="632,162 781,162 796,177 781,192 632,192 647,177" fill="var(--sky)"/>
      <polygon points="805,162 954,162 969,177 954,192 805,192 820,177" fill="var(--navy)"/>
    </g>
    <g stroke="#8a8a8a" stroke-width="1.5">
      <line x1="190" y1="192" x2="190" y2="241"/><line x1="363" y1="192" x2="363" y2="241"/><line x1="536" y1="192" x2="536" y2="241"/><line x1="709" y1="192" x2="709" y2="241"/><line x1="882" y1="192" x2="882" y2="241"/>
    </g>
  </svg>
  <h2 class="heading">OUR PROCESS TO BECOMING YOUR<br><span>PERSONAL CFO</span></h2>
  <div class="step-ring" style="left:134px"><svg width="50" height="50" viewBox="0 0 50 50" fill="none" stroke="var(--navy)" stroke-width="2"><rect x="15" y="8" width="20" height="34"/><path d="M5 42h40M20 14h4M26 14h4M20 22h4M26 22h4M20 30h4M26 30h4"/></svg></div>
  <div class="step-ring" style="left:307px"><svg width="50" height="50" viewBox="0 0 50 50" fill="none" stroke="var(--navy)" stroke-width="2"><rect x="12" y="8" width="22" height="30"/><path d="M17 16h12M17 22h12M17 28h6"/><circle cx="31" cy="32" r="6"/><path d="M35 36l6 6"/></svg></div>
  <div class="step-ring" style="left:480px"><svg width="50" height="50" viewBox="0 0 50 50" fill="none" stroke="var(--navy)" stroke-width="2"><circle cx="30" cy="24" r="9"/><circle cx="30" cy="24" r="3"/><rect x="8" y="8" width="8" height="8"/><path d="M10 12l2 2 3-4"/><rect x="8" y="32" width="8" height="8"/><path d="M10 36l2 2 3-4"/></svg></div>
  <div class="step-ring" style="left:653px"><svg width="50" height="50" viewBox="0 0 50 50" fill="none" stroke="var(--navy)" stroke-width="2"><rect x="8" y="14" width="30" height="26"/><path d="M14 34V28M20 34V24M26 34V20"/><circle cx="38" cy="12" r="6"/></svg></div>
  <div class="step-ring" style="left:826px"><svg width="50" height="50" viewBox="0 0 50 50" fill="none" stroke="var(--navy)" stroke-width="2"><rect x="8" y="10" width="34" height="24"/><path d="M18 40h14M25 34v6M14 28l6-6 5 4 9-9"/></svg></div>
  <div class="step-label" style="left:115px">Establish / Start<br>Relationship</div>
  <div class="step-label" style="left:288px">Gather Info &amp; Analyze</div>
  <div class="step-label" style="left:461px">Develop Plan / Recs</div>
  <div class="step-label" style="left:634px">Implement</div>
  <div class="step-label" style="left:807px">Ongoing Monitoring &amp;<br>Proactive Financial<br>Guidance</div>
  <div class="tagline">Imagine taking a trip without directions</div>
  <div class="cta" style="left:314px;width:190px;background:var(--navy)">You might make it to<br>your destination</div>
  <div class="cta" style="left:550px;width:217px;background:var(--green)">But did you take the<br>best route?</div>
</section>

<!-- Thank you -->
<section class="slide s-thanks">
  <div class="photo" role="img" aria-label="Photo of a financial advisor meeting a client at a laptop" style="left:380px;top:0;width:700px;height:607px;background:linear-gradient(120deg,#8a6a4c,#5d4a3a 45%,#a08772)"></div>
  <svg class="deco" width="1080" height="607" viewBox="0 0 1080 607">
    <polygon points="0,0 300,0 420,0 580,300 420,607 0,607" fill="#fff"/>
    <polygon points="300,0 490,0 665,300 490,607 300,607 470,300" fill="var(--sky)"/>
    <polygon points="300,607 560,240 665,300 490,607" fill="var(--navy)" opacity=".9"/>
    <polygon points="220,0 300,0 180,120" fill="var(--navy)"/>
  </svg>
  <div class="wordmark" style="position:absolute;left:40px;top:150px;font-size:34px"><span class="dot"></span>Clearpath Wealth</div>
  <div class="thanks">THANK YOU</div>
  <div class="presenter">PRESENTER NAME</div>
  <ul class="contacts">
    <li><svg width="14" height="14" viewBox="0 0 14 14"><path d="M3 1l2 3-1.5 1.5a8 8 0 0 0 5 5L10 9l3 2-1 2.5C6 13 1 8 .5 2z" fill="var(--navy)"/></svg>555 010 2090</li>
    <li><svg width="14" height="14" viewBox="0 0 14 14" fill="none" stroke="var(--navy)" stroke-width="1.6"><circle cx="7" cy="7" r="6"/><path d="M1 7h12M7 1c3 3 3 9 0 12M7 1c-3 3-3 9 0 12"/></svg>www.clearpath.example</li>
    <li><svg width="14" height="14" viewBox="0 0 14 14"><rect x="0" y="2" width="14" height="10" fill="var(--navy)"/><path d="M0 2l7 5 7-5" fill="none" stroke="#fff" stroke-width="1.2"/></svg>info@clearpath.example</li>
    <li><svg width="14" height="16" viewBox="0 0 14 16"><path d="M7 0a6 6 0 0 1 6 6c0 4-6 10-6 10S1 10 1 6a6 6 0 0 1 6-6z" fill="var(--navy)"/><circle cx="7" cy="6" r="2" fill="#fff"/></svg>480 Harbor Avenue, Suite 210<br>Riverton, OR 97001</li>
  </ul>
</section>

</body>
</html>
```